Wine Label Design for Marrick Estate

I need a front and back label for a new wine I am making. I am looking for a classic, elegant and serious wine label. I would like the label to be white with blue and black writing. The blue will be the distinction in the label. The color of blue will be unique and catch the eye. The font of the writing will be unique and could also serve as the brand image for Marrick Estate. The label can have a design but should be simple and distinct. I envision the paper quality of the label to textured, high quality and add to the overall image of the label.
The label will be timeless. The price of this wine will be $85.00 a bottle, and the label should match a higher priced wine. This wine is family owned and operated.
The writing on the front and back label will be:

FRONT Label-

Marrick Estate

Howell Mountain

Napa Valley

2022 Cabernet Sauvignon

Back Label-

Cellared and Bottled by Marrick Estate, Calder Ridge, CA 94999

GOVERNMENT WARNING: (1) According to the Surgeon General, women should not drink alcoholic beverages during pregnancy because of the risk of birth defects. (2) Consumption of alcoholic beverages impairs your ability to drive a car or operate machinery, and may cause health problems.

Alc. 14.5% by Vol.

750 ml

Contains Sulfites

```html
<!DOCTYPE html>
<html lang="en">
<head>
<meta charset="utf-8">
<title>Marrick Estate – Wine Labels</title>
<link rel="stylesheet" href="https://fonts.googleapis.com/css2?family=IM+Fell+English+SC&display=swap">
<style>
  :root {
    --backdrop: #000000;
    --paper: #ffffff;
    --ink: #1a1a1a;
    --estate-blue: #2b3190;
    --sulfite-blue: #3c55b6;
    --grape-tone: #3a3f98;
  }
  * { margin: 0; padding: 0; box-sizing: border-box; }
  html, body {
    width: 1200px;
    height: 1132px;
    overflow: hidden;
    background: var(--backdrop);
  }
  .canvas {
    position: relative;
    width: 1200px;
    height: 1132px;
    display: flex;
    justify-content: center;
    align-items: center;
    gap: 48px;
    font-family: "IM Fell English SC", Georgia, serif;
    color: var(--ink);
  }
  .label {
    width: 516px;
    height: 688px;
    background: var(--paper);
    position: relative;
    text-align: center;
  }

  /* Front label */
  .front .vine-art {
    position: absolute;
    left: 50%;
    top: 50px;
    width: 92px;
    height: 162px;
    transform: translateX(-50%);
    background: linear-gradient(180deg, var(--grape-tone), var(--estate-blue));
    border-radius: 46px 46px 40px 40px;
  }
  .front .wordmark {
    position: absolute;
    left: 0; right: 0;
    top: 268px;
    color: var(--estate-blue);
    font-size: 70px;
    font-weight: normal;
    line-height: 76px;
  }
  .front .appellation {
    position: absolute;
    left: 0; right: 0;
    top: 512px;
    font-size: 31px;
    line-height: 42px;
    letter-spacing: 0.5px;
  }
  .front .vintage {
    position: absolute;
    left: 0; right: 0;
    top: 606px;
    color: var(--estate-blue);
    font-size: 22px;
    letter-spacing: 0.5px;
  }

  /* Back label */
  .back .bottler {
    position: absolute;
    left: 0; right: 0;
    top: 70px;
    font-size: 21px;
  }
  .back .producer {
    position: absolute;
    left: 0; right: 0;
    top: 104px;
    color: var(--estate-blue);
    font-size: 34px;
  }
  .back .address {
    position: absolute;
    left: 0; right: 0;
    top: 158px;
    font-size: 22px;
  }
  .back .warning {
    position: absolute;
    left: 60px;
    right: 60px;
    top: 222px;
    text-align: left;
  }
  .warning-title {
    font-size: 24px;
    line-height: 30px;
    margin-bottom: 2px;
    padding-left: 35px;
  }
  .warning-item {
    display: flex;
    font-size: 20.5px;
    line-height: 29px;
    text-align: justify;
    letter-spacing: 0.3px;
  }
  .warning-item .num {
    width: 35px;
    flex: none;
  }
  .back .strength {
    position: absolute;
    left: 0; right: 0;
    top: 515px;
    font-size: 29px;
  }
  .back .volume {
    position: absolute;
    left: 0; right: 0;
    top: 557px;
    font-size: 25px;
  }
  .back .sulfites {
    position: absolute;
    left: 50%;
    top: 613px;
    transform: translateX(-50%);
    background: var(--sulfite-blue);
    color: var(--paper);
    font-size: 19px;
    padding: 1px 12px 2px;
    white-space: nowrap;
  }
</style>
</head>
<body>
<main class="canvas">
  <section class="label front">
    <div class="vine-art" role="img" aria-label="Grape cluster and vine leaf illustration"></div>
    <h1 class="wordmark">Marrick<br>Estate</h1>
    <p class="appellation">Howell Mountain<br>Napa Valley</p>
    <p class="vintage">2022 Cabernet Sauvignon</p>
  </section>

  <section class="label back">
    <p class="bottler">Cellared &amp; Bottled by</p>
    <p class="producer">Marrick Estate</p>
    <p class="address">Calder Ridge, CA 94999</p>
    <div class="warning">
      <p class="warning-title">GOVERNMENT WARNING:</p>
      <p class="warning-item"><span class="num">(1)</span><span>According to the Surgeon General, women should not drink alcoholic beverages during pregnancy because of the risk of birth defects.</span></p>
      <p class="warning-item"><span class="num">(2)</span><span>Consumption of alcoholic beverages impairs your ability to drive a car or operate machinery, and may cause health problems.</span></p>
    </div>
    <p class="strength">Alc. 14.5% by Vol.</p>
    <p class="volume">750 ml</p>
    <p class="sulfites">Contains Sulfites</p>
  </section>
</main>
</body>
</html>
```